Morvadin Nutrition Supplement Jar

Label for jar. White label on a brown bottle jar.
Conservative look, should look like medicine.
Main Side:
Brightfield Health (smaller size) (with logo)
MORVADIN 10mg (large size)
Doctor Formulated
Developed in Clinical Practice
60 Capsules
(I prefer the single color white label with dark brown letters. Please stay close to that design)
(For the back side, please use the multicolor set up)
(The whole Label should be one color - white with dark brown letters)
Please visit my site for more inspiration and feel: www.calmorvex.com
The product will be brown jar listed on this site.
Can you please provide one version without the text "Brightfield Health & Logo".
Thank you.

Target Market(s)

Women, 34-59 years old

Industry/Entity Type

Nutrition

Requirements
Should not have
• Multicolors, leaves,

```html
<!DOCTYPE html>
<html lang="en">
<head>
<meta charset="utf-8">
<title>Morvadin Label Presentation</title>
<link href="https://fonts.googleapis.com/css2?family=Poppins:wght@400;500;600&display=swap" rel="stylesheet">
<style>
  :root {
    --espresso: #2e1813;
    --ink: #2a1510;
    --paper: #ffffff;
    --cream-mark: #f7f2e9;
    --gold: #c9a96a;
    --badge: #3a2a26;
  }
  * { margin: 0; padding: 0; box-sizing: border-box; }
  html, body { width: 1200px; height: 3321px; overflow: hidden; }
  body { font-family: "Poppins", sans-serif; background: var(--paper); }
  .panel { position: relative; width: 1200px; height: 830px; overflow: hidden; }
  .panel--dark { background: var(--espresso); }
  .panel--light { background: var(--paper); }
  .panel--last { height: 831px; }
  .tagline {
    position: absolute; font-weight: 600; font-size: 46px; line-height: 57px;
    letter-spacing: 0.3px;
  }
  .tagline--light { color: var(--paper); left: 116px; top: 330px; }
  .tagline--dark { color: var(--espresso); left: 644px; top: 1160px; top: 330px; }
  .label {
    position: absolute; width: 626px; height: 433px; background: var(--paper);
    box-shadow: 0 6px 22px rgba(0,0,0,0.18); overflow: hidden;
  }
  .label--small { transform: scale(0.56); transform-origin: top left; }
  .label__mark {
    position: absolute; left: 83px; top: 17px; width: 455px; height: 415px;
    border-radius: 45% 45% 40% 40%;
    background: radial-gradient(ellipse at center, var(--cream-mark) 0%, rgba(247,242,233,0.5) 70%, rgba(255,255,255,0) 100%);
  }
  .brand {
    position: absolute; top: 44px; left: 0; width: 100%;
    display: flex; justify-content: center; align-items: center; gap: 10px;
    font-size: 19px; font-weight: 400; color: var(--ink);
  }
  .brand__dot { width: 22px; height: 22px; border-radius: 50%; border: 2px solid var(--gold); }
  .product {
    position: absolute; top: 128px; left: 0; width: 100%;
    display: flex; justify-content: center;
  }
  .product__inner { display: flex; align-items: center; gap: 8px; padding-bottom: 4px; border-bottom: 5px solid var(--ink); }
  .product__name { font-weight: 600; font-size: 58px; line-height: 70px; color: var(--ink); letter-spacing: 1px; }
  .product__dose {
    background: var(--ink); color: var(--paper); font-weight: 600; font-size: 21px;
    padding: 5px 6px; line-height: 28px;
  }
  .claims {
    position: absolute; top: 342px; left: 0; width: 100%; text-align: center;
    font-weight: 600; font-size: 15px; line-height: 20px; color: var(--ink); text-transform: uppercase;
  }
</style>
</head>
<body>

<section class="panel panel--dark">
  <h2 class="tagline tagline--light">Empowering Women<br>Through Balanced<br>Nutrition</h2>
  <div class="label label--small" style="left:700px; top:295px;">
    <div class="label__mark" role="img" aria-label="Faint line drawing of a brain behind the label text"></div>
    <div class="product"><div class="product__inner"><span class="product__name">MORVADIN</span><span class="product__dose">10MG</span></div></div>
    <p class="claims">Doctor Formulated<br>Developed in Clinical Practice<br>60 Capsules</p>
  </div>
</section>

<section class="panel panel--light">
  <div class="label label--small" style="left:168px; top:300px;">
    <div class="label__mark" role="img" aria-label="Faint line drawing of a brain behind the label text"></div>
    <div class="brand"><span class="brand__dot"></span><span>Brightfield Health</span></div>
    <div class="product"><div class="product__inner"><span class="product__name">MORVADIN</span><span class="product__dose">10MG</span></div></div>
    <p class="claims">Doctor Formulated<br>Developed in Clinical Practice<br>60 Capsules</p>
  </div>
  <h2 class="tagline tagline--dark">Empowering Women<br>Through Balanced<br>Nutrition</h2>
</section>

<section class="panel panel--dark">
  <div class="label" style="left:287px; top:198px;">
    <div class="label__mark" role="img" aria-label="Faint line drawing of a brain behind the label text"></div>
    <div class="brand"><span class="brand__dot"></span><span>Brightfield Health</span></div>
    <div class="product"><div class="product__inner"><span class="product__name">MORVADIN</span><span class="product__dose">10MG</span></div></div>
    <p class="claims">Doctor Formulated<br>Developed in Clinical Practice<br>60 Capsules</p>
  </div>
</section>

<section class="panel panel--light panel--last">
  <div class="label" style="left:287px; top:198px;">
    <div class="label__mark" role="img" aria-label="Faint line drawing of a brain behind the label text"></div>
    <div class="product"><div class="product__inner"><span class="product__name">MORVADIN</span><span class="product__dose">10MG</span></div></div>
    <p class="claims">Doctor Formulated<br>Developed in Clinical Practice<br>60 Capsules</p>
  </div>
</section>

</body>
</html>
```